we can communicate on this, but i want to follow the approach we took on Pell|Quorn & Tillet but i feel the card front needs the black background and the platinum and gold logo. The back? I am open. we can use the same info from PQ&T. Vellum Crest is an enhanced equity investment fund - basically a very exclusive boutique hedge fund that uses only stock options. very advanced things. hope you are interested

Contact Information for Business Card

Dr. Owen T. Brisket, CFA
Scientifique de fusée financière
555.014.2296
TheDoc4793@mailvessel.example

4718 Fennel Brook Way N.
Linden Falls, ND 58990

No web site

Colors

Designer to choose colors to be used in the design.

Requirements
Nice to have
• I tend to prefer the most visible applications of the logo to include logo and name, the logo version with a black background and the gold and platinum components separated by the black. I see this working well for a single side (logo and name - this is card front to me).
• I am fairly open to other treatments on the reverse side with the data. To me, it makes sense to have a different color rendition of the logo on the reverse and it may be a muted black tone on tone or an oversized portion that would have spot UV. Or, the reverse may play with colors and layout
Should not have
• Other colors = no no
• Decorative font

```html
<!DOCTYPE html>
<html lang="en">
<head>
<meta charset="utf-8">
<title>Vellum Crest – Business Card</title>
<link rel="stylesheet" href="https://fonts.googleapis.com/css2?family=Montserrat:wght@300;400;600;700;800&display=swap">
<style>
  :root {
    --backdrop: #d0d0cb;
    --paper: #ffffff;
    --black: #141414;
    --ink: #111111;
    --ink-soft: #2b2b2b;
    --gold: #c9a22e;
    --platinum: #d9d9d6;
  }
  * { box-sizing: border-box; margin: 0; padding: 0; }
  html, body {
    width: 1200px; height: 1059px; overflow: hidden;
    background: var(--backdrop);
    font-family: "Montserrat", sans-serif;
  }
  .canvas {
    position: relative; width: 1200px; height: 1059px;
    display: flex; flex-direction: column; align-items: center; justify-content: center;
    gap: 64px;
  }
  .card {
    width: 660px; height: 378px;
    position: relative;
    border-bottom: 4px solid var(--gold);
    box-shadow: 0 14px 30px rgba(0,0,0,0.18);
  }

  /* Front: black, logo and name */
  .card--front {
    background: var(--black);
    display: flex; align-items: center; justify-content: center; gap: 24px;
  }
  .front-mark__dot {
    width: 96px; height: 96px; border-radius: 50%; background: var(--gold); flex: none;
  }
  .front-mark__name {
    font-weight: 800; font-size: 40px; line-height: 1.05; letter-spacing: 1.5px;
    text-transform: uppercase; color: var(--platinum);
  }

  /* Back: contact details */
  .card--back { background: var(--paper); display: flex; align-items: center; }
  .brand {
    width: 300px; display: flex; align-items: center; justify-content: center; gap: 14px;
  }
  .brand__dot {
    width: 52px; height: 52px; border-radius: 50%; background: var(--gold); flex: none;
  }
  .brand__name {
    font-weight: 800; font-size: 26px; line-height: 1.05; letter-spacing: 1px;
    color: var(--ink); text-transform: uppercase;
  }
  .divider { width: 2px; height: 150px; background: var(--gold); flex: none; }
  .contact { padding-left: 34px; padding-right: 20px; color: var(--ink-soft); }
  .contact__name {
    color: var(--gold); font-weight: 600; font-size: 18px; letter-spacing: 1px;
    text-transform: uppercase; white-space: nowrap;
  }
  .contact__title { font-size: 13px; margin-top: 3px; }
  .contact__address { font-size: 13px; line-height: 1.45; margin-top: 14px; }
  .contact__list { list-style: none; margin-top: 14px; font-size: 13px; line-height: 1.65; }
  .contact__list li { display: flex; align-items: center; gap: 9px; white-space: nowrap; }
  .contact__list svg { width: 11px; height: 11px; flex: none; }
</style>
</head>
<body>
<main class="canvas">
  <section class="card card--front" aria-label="Card front">
    <span class="front-mark__dot" aria-hidden="true"></span>
    <span class="front-mark__name">Vellum<br>Crest</span>
  </section>

  <section class="card card--back" aria-label="Card back">
    <div class="brand">
      <span class="brand__dot" aria-hidden="true"></span>
      <span class="brand__name">Vellum<br>Crest</span>
    </div>
    <span class="divider" aria-hidden="true"></span>
    <div class="contact">
      <p class="contact__name">Dr. Owen T. Brisket, CFA</p>
      <p class="contact__title">Scientifique de fusée financière</p>
      <p class="contact__address">4718 Fennel Brook Way N.<br>Linden Falls, ND 58990</p>
      <ul class="contact__list">
        <li>
          <svg viewBox="0 0 12 12" aria-hidden="true"><path d="M2.5 1 L4.5 1 L5 3.5 L3.8 4.4 Q4.8 6.8 7.6 8.2 L8.5 7 L11 7.5 L11 9.5 Q10.5 11 9 11 Q1 10 1 2.5 Q1 1 2.5 1 Z" fill="var(--gold)"/></svg>
          555.014.2296
        </li>
        <li>
          <svg viewBox="0 0 12 12" aria-hidden="true"><rect x="1" y="2.5" width="10" height="7" fill="none" stroke="var(--gold)" stroke-width="1.2"/><path d="M1 2.5 L6 6.5 L11 2.5" fill="none" stroke="var(--gold)" stroke-width="1.2"/></svg>
          TheDoc4793@mailvessel.example
        </li>
      </ul>
    </div>
  </section>
</main>
</body>
</html>
```